Talkbridge Allies co-marketing flier

We want a flier that our partners (IT consultants) can hand out to their clients and that we can send to local businesses on their behalf to demonstrate that they can help customers purchase a phone system that has professional features that they would expect in a phone solution that costs thousands of dollars.

We want the brochure to look very professional with excellent layout and use of space.

The Talkbridge Allies corporate colour is green and more details can be found at www.talkbridgeallies.com.au.

We have attached a draft Word document that contains most of the information we need but please present the information in the way YOU believe it should be laid out.

We are looking for a designer who understands the concept and uses their own skills to produce a work of art.

Target Market(s)

small businesses that want to save money but also want a modern phone with lots of features

Industry/Entity Type

Marketing

Requirements
Must have
• Must have an image of the main phone and a cordless handset to indicate that they don't need wires to set the system up.

Must have our logo and website address

Must have a box or some "placeholder" where our partners can stamp or insert their details.

Must have a "call to action" saying "Contact us for a quote"

```html
<!DOCTYPE html>
<html lang="en">
<head>
<meta charset="utf-8">
<title>Talkbridge Allies – Phone System Flier</title>
<link href="https://fonts.googleapis.com/css2?family=Open+Sans:wght@400;600;700&family=Oswald:wght@500;700&display=swap" rel="stylesheet">
<style>
  :root {
    --green: #2f8a2c;
    --green-dark: #1f6a1c;
    --green-light: #5fc24f;
    --line: #3a8e34;
    --ink: #333;
    --paper: #ffffff;
    --grey: #c9c9c9;
    --frame: #9a9a9a;
  }
  * { box-sizing: border-box; margin: 0; padding: 0; }
  html, body { width: 849px; height: 1200px; overflow: hidden; }
  body { font-family: "Open Sans", Arial, sans-serif; color: var(--ink); }
  .flier {
    position: relative; width: 849px; height: 1200px; overflow: hidden;
    background:
      radial-gradient(ellipse 55% 45% at 52% 35%, #ffffff 0%, rgba(255,255,255,0) 100%),
      linear-gradient(90deg, #d0d0d0 0%, #f4f4f4 30%, #f6f6f6 70%, #cfcfcf 100%);
  }
  .flier::after {
    content: ""; position: absolute; left: 0; right: 0; bottom: 0; height: 220px;
    background: linear-gradient(180deg, rgba(200,200,200,0) 0%, rgba(195,195,195,.7) 100%);
    pointer-events: none;
  }
  .product-photo {
    position: absolute; left: 130px; top: 30px; width: 660px; height: 290px;
    border-radius: 40px;
    background: radial-gradient(ellipse at 60% 45%, #d8d8d8 0%, #a9a9a9 55%, rgba(230,230,230,0) 75%);
  }
  .connectors { position: absolute; inset: 0; z-index: 1; }
  .bubble {
    position: absolute; z-index: 2; border-radius: 50%;
    display: flex; align-items: center; justify-content: center; text-align: center;
    color: #fff; text-transform: uppercase; font-size: 19px; line-height: 1.3;
    background: radial-gradient(circle at 50% 70%, var(--green-light) 0%, var(--green) 55%, var(--green-dark) 100%);
    border: 3px solid #fff;
    box-shadow: 0 4px 12px rgba(0,0,0,.35), inset 0 0 0 2px rgba(0,0,0,.15);
    overflow: hidden;
  }
  .bubble::before {
    content: ""; position: absolute; left: 14%; top: 4%; width: 72%; height: 42%;
    border-radius: 50%;
    background: linear-gradient(180deg, rgba(255,255,255,.55), rgba(255,255,255,.05));
  }
  .bubble span { position: relative; }
  .bubble-question { left: 194px; top: 244px; width: 196px; height: 196px; font-size: 21px; }
  .bubble-why { left: 20px; top: 478px; width: 142px; height: 142px; }
  .bubble-features { left: 410px; top: 418px; width: 146px; height: 146px; font-size: 20px; }
  .bubble-contact { left: 94px; top: 950px; width: 138px; height: 138px; font-size: 16px; }
  .tag {
    position: absolute; z-index: 3; background: var(--green); border: 2px solid #fff;
    border-radius: 4px; box-shadow: 0 2px 5px rgba(0,0,0,.3);
    display: flex; align-items: center; justify-content: center; color: #fff;
    font-weight: 700;
  }
  .tag-phone { left: 398px; top: 314px; width: 56px; height: 54px; }
  .tag-help { left: 160px; top: 535px; width: 40px; height: 36px; font-size: 22px; }
  .tag-plus { left: 550px; top: 473px; width: 40px; height: 37px; font-size: 30px; }
  .tag-mail { left: 54px; top: 1003px; width: 36px; height: 34px; font-size: 20px; }
  .panel {
    position: absolute; z-index: 2; background: var(--green); color: #fff;
    border-radius: 6px; box-shadow: 0 3px 8px rgba(0,0,0,.2);
  }
  .panel-why { left: 124px; top: 575px; width: 288px; height: 283px; padding: 38px 26px 0 26px; }
  .panel-why p { font-family: "Oswald", Impact, sans-serif; font-weight: 500; font-size: 14.5px; line-height: 1.45; }
  .panel-why .punchline {
    font-family: "Oswald", Impact, sans-serif; font-weight: 700; font-size: 31px;
    line-height: 1.25; text-align: center; margin-top: 38px;
  }
  .features-note { position: absolute; left: 557px; top: 516px; color: var(--green); font-size: 16px; z-index: 2; }
  .panel-features { left: 494px; top: 541px; width: 312px; height: 284px; padding: 26px 16px 0 28px; }
  .feature-list { list-style: none; font-size: 14.5px; line-height: 1.4; }
  .feature-list li { position: relative; padding-left: 32px; margin-bottom: 7px; }
  .feature-list li::before {
    content: "+"; position: absolute; left: 0; top: -5px; font-size: 24px; font-weight: 700;
  }
  .brand { position: absolute; left: 240px; top: 975px; z-index: 2; }
  .brand-name { font-size: 30px; font-weight: 700; color: var(--green); letter-spacing: -.5px; line-height: 1.1; }
  .brand-entity { font-size: 13px; margin-top: 6px; }
  .brand-abn { font-size: 10.5px; }
  .brand-web { font-size: 13px; }
  .partner-stamp {
    position: absolute; left: 491px; top: 962px; width: 315px; height: 115px; z-index: 2;
    background: rgba(255,255,255,.85); border: 2px solid var(--frame); border-radius: 10px;
  }
</style>
</head>
<body>
<main class="flier">
  <div class="product-photo" role="img" aria-label="Photo of a cordless handset in its cradle beside a desk phone with display and coiled handset cord"></div>

  <svg class="connectors" width="849" height="1200" viewBox="0 0 849 1200" aria-hidden="true">
    <g fill="none" stroke="var(--line)" stroke-width="3">
      <polyline points="210,392 90,392 90,480"/>
      <polyline points="158,520 290,520 290,483 412,483"/>
      <polyline points="484,562 484,905 158,905 158,952"/>
    </g>
  </svg>

  <div class="bubble bubble-question"><span>Looking for<br>a new phone<br>system?</span></div>
  <div class="tag tag-phone" aria-hidden="true">
    <svg width="30" height="30" viewBox="0 0 24 24"><path fill="#fff" d="M6.6 10.8a15.2 15.2 0 0 0 6.6 6.6l2.2-2.2c.3-.3.7-.4 1-.2 1.1.4 2.3.6 3.6.6.6 0 1 .4 1 1V20c0 .6-.4 1-1 1A17 17 0 0 1 3 4c0-.6.4-1 1-1h3.5c.6 0 1 .4 1 1 0 1.3.2 2.5.6 3.6.1.3 0 .7-.2 1z"/></svg>
  </div>

  <div class="bubble bubble-why"><span>Why us?</span></div>
  <div class="tag tag-help" aria-hidden="true">?</div>
  <section class="panel panel-why">
    <p>Our proven VoIP solution comes with all the professional features to service an office of up to 6 people.</p>
    <p class="punchline">It’s cheaper than you think.</p>
  </section>

  <div class="bubble bubble-features"><span>Features</span></div>
  <div class="tag tag-plus" aria-hidden="true">+</div>
  <p class="features-note">includes, but not limited to:</p>
  <section class="panel panel-features">
    <ul class="feature-list">
      <li>very low line rental rates*</li>
      <li>10c local and national calls untimed</li>
      <li>voicemail-to-email</li>
      <li>direct in-dial to every extension</li>
      <li>number portability (keep your number when you move)</li>
      <li>call records via spreadsheet</li>
      <li>flat rate local and national calls</li>
    </ul>
  </section>

  <div class="bubble bubble-contact"><span>Contact us<br>for a quote</span></div>
  <div class="tag tag-mail" aria-hidden="true">@</div>
  <div class="brand">
    <p class="brand-name">Talkbridge Allies</p>
    <p class="brand-entity">corvane (456 Holdings Pty Ltd)</p>
    <p class="brand-abn">ABN: 12 345 678 901</p>
    <p class="brand-web">www.talkbridgeallies.com.au</p>
  </div>

  <div class="partner-stamp" aria-label="Space for partner details"></div>
</main>
</body>
</html>
```